Fernlymentor: an app for coaches and students in golf and fitness

I currently have an app that is called Fernlymentor and I am redoing the app completely and with this I am looking for a cool design for the app. I am not happy with the design as it is at the moment. The app should have a nice welcome and when you are logged in the dashboard must be very modern. It is a golf app that have 2 type of users. 1 user is the coach and the other user is the student. Those users can see different things of course.
The coach is normally paying a subscription charge for using the app but I want to get the students to pay for different tools that I will be offering via the app. To me the dashboard and the homepage of the app (once you have downloaded the app) is important. Here I would like to get the student as well as the coach the feeling of what the app can offer. The app offers features like Calendar (here the student can book the coach via the calendar), Chat (here the coach and the student can chat with each other as well as the coach can creat group chats with several students), Notes (here the coach as well as the student can create notes for their lessons), video tips (here the coach can upload video tips for his/her students, online lesson (the student can take online lessons by uploading recorded videos..and so on

Target Market(s)

Sport coaches (for start it will be mostly golf coaches)

Industry/Entity Type

Sports

Font styles to use
Sans Serif

Colors
0054AA
0677BA
7BADD7
CADEEF
E8F1F8

Requirements
Must have
• modern design and easy navigation.
Nice to have
• It all starts with the dashboard
Should not have
• boring standard style.

```html
<!DOCTYPE html>
<html lang="en">
<head>
<meta charset="utf-8">
<title>Fernlymentor app screens</title>
<link href="https://fonts.googleapis.com/css2?family=Poppins:wght@600;700&family=Roboto:wght@400;500;700&display=swap" rel="stylesheet">
<style>
:root{
  --stage:#0d6377;
  --deep:#0e6277;
  --accent:#6fc3e3;
  --pale:#cfeaf6;
  --ink:#1b1b1b;
  --muted:#9a9a9a;
  --line:#ececec;
  --white:#ffffff;
}
*{box-sizing:border-box;margin:0;padding:0}
html,body{width:1200px;height:686px;overflow:hidden;background:var(--stage);font-family:"Roboto",sans-serif;color:var(--ink)}
.screen{position:absolute;top:111px;width:214px;height:464px;border-radius:10px;overflow:hidden;background:#f8f8f8;box-shadow:0 6px 18px rgba(0,0,0,.18)}
.abs{position:absolute}

/* splash */
.splash{left:19px;background:radial-gradient(ellipse at 10% 100%,#c6e7f5 0,rgba(198,231,245,0) 55%),radial-gradient(ellipse at 80% 5%,#d3e3e8 0,rgba(211,227,232,0) 50%),#f9fbfc}
.wordmark{left:0;right:0;top:223px;display:flex;align-items:center;justify-content:center;gap:5px;font-family:"Roboto",sans-serif;font-weight:700;font-size:18px;color:var(--deep)}
.wordmark .dot{width:14px;height:14px;border-radius:50%;background:var(--accent)}

/* registration */
.register{left:256px;background:radial-gradient(ellipse at 15% 100%,#c6e7f5 0,rgba(198,231,245,0) 55%),radial-gradient(ellipse at 85% 8%,#d0e0e5 0,rgba(208,224,229,0) 50%),#f9fbfc;text-align:center}
.register .center{left:0;right:0}
.welcome{top:87px;font-size:16px;font-weight:500}
.brand-name{top:109px;font-size:22px;font-weight:700;color:var(--accent)}
.tagline{top:145px;font-size:7.4px;color:#666}
.reg-title{top:222px;font-size:16px;font-weight:500;color:#333}
.reg-question{top:253px;font-size:11px;color:#444}
.role{top:284px;width:74px;height:74px;border-radius:8px;background:var(--white);box-shadow:0 2px 8px rgba(0,0,0,.06);font-size:8.5px;color:#444}
.role .figure{position:absolute;left:22px;top:12px;width:30px;height:36px;border-radius:6px;background:#bfe3f2}
.role span{position:absolute;left:0;right:0;top:56px}
.role.coach{left:27px}
.role.student{left:113px;background:linear-gradient(135deg,#0e6277 0%,#2d8fae 60%,#74c6e4 100%);color:var(--white)}
.role.student .figure{background:rgba(255,255,255,.55)}
.login{left:26px;top:390px;width:162px;height:29px;border-radius:5px;background:var(--deep);color:var(--white);font-size:8px;font-weight:700;line-height:29px;letter-spacing:.3px}

/* dashboard */
.dashboard{left:493px}
.menu{left:10px;top:31px}
.screen-title{font-family:"Poppins",sans-serif;font-weight:700;font-size:15px}
.dashboard .screen-title{left:32px;top:24px}
.tile{width:91px;height:97px;border-radius:8px;background:var(--white);box-shadow:0 2px 8px rgba(0,0,0,.05);padding:55px 9px 0}
.tile .icon{position:absolute;left:9px;top:11px;width:22px;height:22px;border-radius:4px;background:#d3edf7}
.tile h3{font-size:8.5px;font-weight:500;margin-top:-13px;white-space:nowrap}
.tile p{font-size:6px;line-height:9px;color:var(--muted);margin-top:5px}
.tile.active{background:linear-gradient(135deg,#0e6277 0%,#2d8fae 55%,#74c6e4 100%);color:var(--white)}
.tile.active p{color:#e6f5fb}
.tile.active .icon{background:rgba(255,255,255,.55)}
.c1{left:10px}.c2{left:113px}
.r1{top:62px}.r2{top:171px}.r3{top:279px}.r4{top:388px}

/* calendar */
.calendar{background:var(--white)}
.cal-a{left:730px}.cal-b{left:967px}
.back{left:10px;top:30px}
.calendar .screen-title{left:32px;top:24px;font-size:16px}
.tools{right:12px;top:29px;display:flex;gap:9px}
.week{left:4px;right:4px;top:55px;display:grid;grid-template-columns:repeat(7,1fr);text-align:center}
.week .dl{font-size:6.5px;color:#333}
.week .dn{font-size:10px;margin-top:10px;height:23px;line-height:23px}
.week .today{display:inline-block;width:23px;height:23px;border-radius:50%;background:var(--deep);color:var(--white);font-weight:700}
.week .sat{color:#aaa}.week .sun{color:var(--accent)}
.day-label{left:0;right:0;top:100px;text-align:center;font-size:9.5px;color:#222}
.grid{left:0;right:0;top:118px}
.hour{height:34.3px;border-top:1px solid var(--line);font-size:8.3px;padding:12px 0 0 15px;color:#333}
.lesson{left:47px;top:118px;width:157px;height:69px;background:var(--pale);border-left:3px solid #8fd0ea;font-size:9px;font-weight:700;padding:5px 6px}
.fab{left:169px;top:403px;width:34px;height:34px;border-radius:50%;background:radial-gradient(circle at 40% 35%,#5cc0df,#1e8aa8);box-shadow:0 3px 8px rgba(0,0,0,.2)}
.fab svg{position:absolute;left:10px;top:10px}
.shade{inset:0;background:rgba(90,90,90,.62)}
.picker{left:16px;top:134px;width:183px;height:197px;background:var(--white);border-radius:9px}
.picker-head{left:0;right:0;top:14px;text-align:center;font-size:11px;color:#333}
.picker-head .arrow{position:absolute;top:3px}
.days{left:9px;right:9px;top:58px;display:grid;grid-template-columns:repeat(7,1fr);row-gap:9.5px;text-align:center;font-size:8px;color:#333}
.days .wd{color:#888;margin-bottom:4px}
.days .sel{justify-self:center;width:14px;height:14px;line-height:14px;border-radius:50%;background:#0054aa;color:var(--white)}
.days .now{color:var(--accent);font-weight:700}
</style>
</head>
<body>

<section class="screen splash">
  <div class="abs wordmark"><span class="dot"></span>Fernlymentor</div>
</section>

<section class="screen register">
  <h2 class="abs center welcome">Welcome to</h2>
  <h1 class="abs center brand-name">Fernlymentor</h1>
  <p class="abs center tagline">Registrartion is your first step in getting better</p>
  <h2 class="abs center reg-title">Registration</h2>
  <p class="abs center reg-question">Are you a?</p>
  <div class="abs role coach"><div class="figure" role="img" aria-label="Coach line icon"></div><span>Coach</span></div>
  <div class="abs role student"><div class="figure" role="img" aria-label="Student line icon"></div><span>Student</span></div>
  <div class="abs login">LOGIN</div>
</section>

<section class="screen dashboard">
  <svg class="abs menu" width="11" height="9" viewBox="0 0 11 9"><path d="M0 .7h11M0 4.5h11M0 8.3h11" stroke="#222" stroke-width="1.2"/></svg>
  <h1 class="abs screen-title">Dashboard</h1>
  <div class="abs tile c1 r1"><div class="icon" role="img" aria-label="Calendar icon"></div><h3>My Calendar</h3><p>Book and manage your appointments 24/7</p></div>
  <div class="abs tile c2 r1"><div class="icon" role="img" aria-label="Online lessons icon"></div><h3>Online Lessons</h3><p>Edit and view your students online lessons</p></div>
  <div class="abs tile c1 r2"><div class="icon" role="img" aria-label="Products icon"></div><h3>My Products</h3><p>Configure lessons detail for calendar and online lesson</p></div>
  <div class="abs tile c2 r2 active"><div class="icon" role="img" aria-label="Students icon"></div><h3>My Students</h3><p>Find all info of your students</p></div>
  <div class="abs tile c1 r3"><div class="icon" role="img" aria-label="Offers icon"></div><h3>My Offers</h3><p>Here pro can offer provide info to his/her students</p></div>
  <div class="abs tile c2 r3"><div class="icon" role="img" aria-label="Bird icon"></div><h3>Mentor365</h3><p>Here pro can offer provide info to his/her students</p></div>
  <div class="abs tile c1 r4"><div class="icon" role="img" aria-label="Video editor icon"></div><h3>Video Editor</h3><p>Some Description....</p></div>
</section>

<section class="screen calendar cal-a">
  <svg class="abs back" width="12" height="10" viewBox="0 0 12 10"><path d="M11 5H1.5M5.5 1 1.5 5l4 4" fill="none" stroke="#222" stroke-width="1.3"/></svg>
  <h1 class="abs screen-title">April</h1>
  <div class="abs tools">
    <svg width="11" height="11" viewBox="0 0 11 11"><rect x="1" y="2" width="9" height="8" rx="1" fill="none" stroke="#222" stroke-width="1.2"/><path d="M1 4.5h9M3.5 .5v2.5M7.5 .5v2.5" stroke="#222" stroke-width="1.2"/></svg>
    <svg width="11" height="11" viewBox="0 0 11 11"><circle cx="4.5" cy="4.5" r="3.6" fill="none" stroke="#222" stroke-width="1.3"/><path d="M7.2 7.2 10.5 10.5" stroke="#222" stroke-width="1.4"/></svg>
    <svg width="11" height="11" viewBox="0 0 11 11"><circle cx="5.5" cy="5.5" r="3.8" fill="none" stroke="#222" stroke-width="1.8" stroke-dasharray="2 1"/><circle cx="5.5" cy="5.5" r="1.5" fill="none" stroke="#222" stroke-width="1.1"/></svg>
  </div>
  <div class="abs week">
    <div><div class="dl">M</div><div class="dn">18</div></div>
    <div><div class="dl">T</div><div class="dn"><span class="today">19</span></div></div>
    <div><div class="dl">W</div><div class="dn">20</div></div>
    <div><div class="dl">T</div><div class="dn">21</div></div>
    <div><div class="dl">F</div><div class="dn">22</div></div>
    <div><div class="dl sat">S</div><div class="dn sat">23</div></div>
    <div><div class="dl sun">S</div><div class="dn sun">24</div></div>
  </div>
  <p class="abs day-label">Tuesday 19, April 2022</p>
  <div class="abs grid">
    <div class="hour">12AM</div><div class="hour">1AM</div><div class="hour">2AM</div><div class="hour">3AM</div><div class="hour">4AM</div>
    <div class="hour">5AM</div><div class="hour">6AM</div><div class="hour">7AM</div><div class="hour">8AM</div><div class="hour">9AM</div>
  </div>
  <div class="abs lesson">Lesson</div>
  <div class="abs fab"><svg width="14" height="14" viewBox="0 0 14 14"><path d="M7 0v14M0 7h14" stroke="#fff" stroke-width="1.4"/></svg></div>
</section>

<section class="screen calendar cal-b">
  <svg class="abs back" width="12" height="10" viewBox="0 0 12 10"><path d="M11 5H1.5M5.5 1 1.5 5l4 4" fill="none" stroke="#222" stroke-width="1.3"/></svg>
  <h1 class="abs screen-title">April</h1>
  <div class="abs tools">
    <svg width="11" height="11" viewBox="0 0 11 11"><rect x="1" y="2" width="9" height="8" rx="1" fill="none" stroke="#222" stroke-width="1.2"/><path d="M1 4.5h9M3.5 .5v2.5M7.5 .5v2.5" stroke="#222" stroke-width="1.2"/></svg>
    <svg width="11" height="11" viewBox="0 0 11 11"><circle cx="4.5" cy="4.5" r="3.6" fill="none" stroke="#222" stroke-width="1.3"/><path d="M7.2 7.2 10.5 10.5" stroke="#222" stroke-width="1.4"/></svg>
    <svg width="11" height="11" viewBox="0 0 11 11"><circle cx="5.5" cy="5.5" r="3.8" fill="none" stroke="#222" stroke-width="1.8" stroke-dasharray="2 1"/><circle cx="5.5" cy="5.5" r="1.5" fill="none" stroke="#222" stroke-width="1.1"/></svg>
  </div>
  <div class="abs week">
    <div><div class="dl">M</div><div class="dn">18</div></div>
    <div><div class="dl">T</div><div class="dn"><span class="today">19</span></div></div>
    <div><div class="dl">W</div><div class="dn">20</div></div>
    <div><div class="dl">T</div><div class="dn">21</div></div>
    <div><div class="dl">F</div><div class="dn">22</div></div>
    <div><div class="dl sat">S</div><div class="dn sat">23</div></div>
    <div><div class="dl sun">S</div><div class="dn sun">24</div></div>
  </div>
  <p class="abs day-label">Tuesday 19, April 2022</p>
  <div class="abs grid">
    <div class="hour">12AM</div><div class="hour">1AM</div><div class="hour">2AM</div><div class="hour">3AM</div><div class="hour">4AM</div>
    <div class="hour">5AM</div><div class="hour">6AM</div><div class="hour">7AM</div><div class="hour">8AM</div><div class="hour">9AM</div>
  </div>
  <div class="abs lesson">Lesson</div>
  <div class="abs fab"><svg width="14" height="14" viewBox="0 0 14 14"><path d="M7 0v14M0 7h14" stroke="#fff" stroke-width="1.4"/></svg></div>
  <div class="abs shade"></div>
  <div class="abs picker">
    <div class="abs picker-head">
      <svg class="arrow" style="left:36px" width="5" height="8" viewBox="0 0 5 8"><path d="M5 0v8L0 4z" fill="#777"/></svg>
      January 2023
      <svg class="arrow" style="right:36px" width="5" height="8" viewBox="0 0 5 8"><path d="M0 0v8l5-4z" fill="#777"/></svg>
    </div>
    <div class="abs days">
      <span class="wd">S</span><span class="wd">M</span><span class="wd">T</span><span class="wd">W</span><span class="wd">T</span><span class="wd">F</span><span class="wd">S</span>
      <span></span><span></span><span>1</span><span>2</span><span>3</span><span>4</span><span>5</span>
      <span>6</span><span>7</span><span>8</span><span>9</span><span>10</span><span>11</span><span>12</span>
      <span>13</span><span class="sel">14</span><span>15</span><span class="now">16</span><span>17</span><span>18</span><span>19</span>
      <span>20</span><span>21</span><span>22</span><span>23</span><span>24</span><span>25</span><span>26</span>
      <span>27</span><span>28</span><span>29</span><span>30</span>
    </div>
  </div>
</section>

</body>
</html>
```